Comedy Hypnotist Lionel K Show Poster

I need a poster that can send to clubs that book my show for them in turn to use to promote me/my show at their club. The poster needs to be fun and attractive, and to have a blank space at the bottom where the club(s) can add the details particular to their show. [You'll have seen these posters everywhere for bands etc.]

I'm not fussy about whether or not you use the colours from my website or any of my photos. But do capture at least the essence of the logo somewhere.

I am not like other hypnotists - I want to convey an image of amazing hilarious fun, that everyone can enjoy. [NO Watches, NO Chickens and NO Spirals]. My show is hilarious and clean.

I come across as a little geeky, and very professional. Not sleazy or creepy. But fun, professional and easy to deal with. The show is loud, buzzy and amazing. People literally laugh until they cry. I use great lighting and amazing sound to make it a real event. I aim to entertain everyone. I am never mean and don't pick on or exploit people. (Check the website for video links and more images as well as the crap posters I use now) www.lionelk-stage.net.

Somehow I want people who see my poster to go - that looks like fun! Lets check it out. I would so totally go to that.

It's worth looking at the website and the youtube vid to get a feel for what I do. The pictures you'll see are colourful and active.

My logo is newish - I like it because it is simple, professional and elegant - and different from other hypnotists. In a way that is my main marketing angle - I am different from other hypnotists.

Posters should be international paper A3 size.

Target Market(s)

entertainment, comedy, hypnotist

Industry/Entity Type

Entertainment Industry

Font styles to use
Sans Serif

Requirements
Must have
• Space at the bottom (white space) for people to write the details of their event on.
• "www.lionelk-stage.net" in case they want to look me up.
• "Comedy Hypnotist"
• "Lionel K"
Nice to have
• Simple and clean designs. You don't have to use the logo but if you reference it somehow that would be better so they tie together. I have included some studio photos of myself but these are not required for the poster. You can choose not to include any picture - they are there for if you want them for your design idea.
Should not have
• Spirals, Watches, Chickens

```html
<!DOCTYPE html>
<html lang="en">
<head>
<meta charset="UTF-8">
<title>Comedy Hypnotist Lionel K – Show Poster</title>
<link rel="stylesheet" href="https://fonts.googleapis.com/css2?family=Encode+Sans:wght@400;900&family=Lexend:wght@600&display=swap">
<style>
  :root {
    --sky-top: #fbe584;
    --sky-mid: #e9b95a;
    --sky-bottom: #cb8731;
    --hot-pink: #e4198b;
    --royal-blue: #2855a4;
    --suit-dark: #2a2724;
    --suit-light: #4a4540;
  }
  html, body {
    margin: 0;
    padding: 0;
    width: 800px;
    height: 1200px;
    overflow: hidden;
  }
  .poster {
    position: relative;
    width: 800px;
    height: 1200px;
    background: linear-gradient(180deg, var(--sky-top) 0%, var(--sky-mid) 55%, var(--sky-bottom) 100%);
    font-family: "Encode Sans", Arial, sans-serif;
    overflow: hidden;
  }
  .headline {
    position: absolute;
    top: 14px;
    left: 0;
    width: 100%;
    margin: 0;
    text-align: center;
    font-weight: 400;
    font-size: 66px;
    letter-spacing: 0.5px;
    color: var(--hot-pink);
    line-height: 1;
  }
  .performer-name {
    position: absolute;
    top: 78px;
    left: 0;
    width: 100%;
    margin: 0;
    text-align: center;
    font-weight: 900;
    font-size: 150px;
    letter-spacing: -2px;
    color: var(--royal-blue);
    line-height: 1;
  }
  .tagline {
    position: absolute;
    top: 232px;
    left: 0;
    width: 100%;
    margin: 0;
    text-align: center;
    font-weight: 400;
    font-size: 27px;
    color: var(--hot-pink);
    line-height: 1;
  }
  .performer-photo {
    position: absolute;
    top: 282px;
    left: 282px;
    width: 268px;
    height: 676px;
    border-radius: 40px;
    background: linear-gradient(180deg, var(--suit-light) 0%, var(--suit-dark) 100%);
    opacity: 0.85;
  }
  .website {
    position: absolute;
    top: 952px;
    left: 0;
    width: 100%;
    margin: 0;
    text-align: center;
    font-family: "Lexend", Arial, sans-serif;
    font-weight: 600;
    font-size: 50px;
    color: var(--royal-blue);
    line-height: 1.2;
  }
</style>
</head>
<body>
  <main class="poster">
    <h2 class="headline">COMEDY HYPNOTIST</h2>
    <h1 class="performer-name">LIONEL K</h1>
    <p class="tagline">COMEDY HYPNOTIST SHOWS FOR ANYONE, ANYWHERE</p>
    <div class="performer-photo" role="img" aria-label="Full-length studio photo of the performer in glasses, white shirt, black waistcoat and trousers, smiling and pointing at the viewer"></div>
    <p class="website">www.lionelk-stage.net</p>
  </main>
</body>
</html>
```